VentriLedger.Com PowerPoint

I need a PowerPoint layout for my presentations. My business is called VentriLedger.Com - my presentations teach cardiologists how to document their procedures and visits and teaches them how to bill accurately for them.

Industry/Entity Type

Business

Requirements
Must have
• the logo should be subtly there on each page - perhaps as a watermark? I'm really not creative; please help.

```html
<!DOCTYPE html>
<html lang="en">
<head>
<meta charset="utf-8">
<title>VentriLedger.Com Presentation Template</title>
<link rel="stylesheet" href="https://fonts.googleapis.com/css2?family=Montserrat:wght@600;700&family=Arimo:ital,wght@0,400;0,700;1,400&family=Shadows+Into+Light&display=swap">
<style>
:root{
  --red:#c8192a;
  --red-light:#e4232c;
  --red-deep:#8c0b16;
  --red-bright:#e8242e;
  --orange:#ee5a2c;
  --gold:#f4a51c;
  --ink:#1b1b1b;
  --text:#333;
  --gray:#a8a8a8;
  --paper:#ffffff;
  --canvas:#f1f1f1;
}
*{margin:0;padding:0;box-sizing:border-box}
html,body{width:797px;height:1200px;overflow:hidden}
body{background:var(--canvas);position:relative;font-family:"Arimo",Arial,sans-serif;color:var(--text)}

.slide{position:absolute;width:368px;height:278px;overflow:hidden;background:var(--paper);box-shadow:0 0 0 1px #dcdcdc}
.slide--red{background:radial-gradient(circle at 70% 25%,#d72636,#b8121f 75%)}
.col-left{left:25px}.col-right{left:404px;width:369px}
.row-1{top:20px}.row-2{top:311px}.row-3{top:606px}.row-4{top:897px}

/* shared title */
.slide-heading{position:absolute;left:27px;top:28px;font-family:"Montserrat",sans-serif;font-weight:700;font-size:12px;color:var(--ink);line-height:1}
.slide-heading small{display:block;font-family:"Arimo",sans-serif;font-weight:400;font-size:9px;color:var(--orange);margin-top:3px}
.body-copy{position:absolute;font-size:5.7px;line-height:1.38;color:var(--text)}
.body-copy p+p{margin-top:6px}

/* footer */
.slide-footer{position:absolute;left:0;right:0;bottom:0;height:31px;background:linear-gradient(90deg,#7a0912,#a3111d 60%,#7d0a13);color:#fff}
.footer-logo{position:absolute;left:8px;top:9px;font-family:"Montserrat",sans-serif;font-weight:700;font-size:8.5px;letter-spacing:.2px}
.footer-title{position:absolute;left:135px;top:8px;padding-left:8px;border-left:1px solid rgba(255,255,255,.25);height:16px}
.footer-title b{display:block;font-weight:400;font-size:8.5px;line-height:1}
.footer-title small{display:block;font-size:4.5px;margin-top:1px}
.footer-by{position:absolute;left:232px;top:12px;font-size:5.5px;color:var(--gold)}
.page-num{position:absolute;right:0;bottom:0;width:46px;height:52px;background:var(--red-bright);clip-path:polygon(100% 0,100% 100%,0 100%);color:#fff;font-family:"Montserrat",sans-serif;font-weight:700;font-size:12px;text-align:right;padding:30px 9px 0 0}

/* cover & closing */
.ribbon{position:absolute;left:0;top:72px;width:346px;height:140px;border-radius:0 16px 16px 0;background:linear-gradient(90deg,#b0121d,#e4232c);overflow:hidden}
.ribbon-base{position:absolute;left:0;right:0;bottom:0;height:36px;background:linear-gradient(90deg,#8c0b16,#6f0810)}
.cover-title{position:absolute;left:140px;top:84px;font-family:"Montserrat",sans-serif;font-weight:700;font-size:34px;color:#fff;line-height:1;letter-spacing:-.5px}
.cover-rule{position:absolute;left:140px;top:124px;width:192px;height:1px;background:rgba(255,255,255,.7)}
.cover-name{position:absolute;left:180px;top:127px;font-size:16px;color:#fff}
.cover-sub{position:absolute;left:193px;top:146px;font-size:8px;color:#fff}
.cover-by{position:absolute;left:252px;top:159px;font-size:5.5px;color:var(--gold)}
.brand-mark{position:absolute;font-family:"Montserrat",sans-serif;font-weight:700;color:#fff;font-size:11px}

/* slide 1 */
.avatar{position:absolute;border-radius:50%;border:2px solid #fff;box-shadow:0 1px 4px rgba(0,0,0,.35);background:radial-gradient(circle at 50% 40%,#d9b9a0,#6d5447 70%)}
.callout{position:absolute;height:18px;background:var(--red-bright);color:#fff;font-size:7px;border-radius:2px;padding:5px 0 0 10px}
.dot{position:absolute;width:4px;height:4px;border-radius:50%;background:var(--red-bright)}

/* slide 2 */
.bubble{position:absolute;border-radius:50%;background:var(--gray);color:#f4f4f4;font-size:5.8px;line-height:1.35;text-align:center}
.bubble b{font-weight:700;color:#fff}

/* break */
.cup{position:absolute;left:24px;top:56px;width:100px;height:124px;border-radius:10px;background:linear-gradient(180deg,rgba(255,255,255,.12),rgba(255,255,255,.35))}
.break-title{position:absolute;left:180px;top:79px;font-family:"Montserrat",sans-serif;font-weight:700;font-size:31px;color:#fff;letter-spacing:-.5px;line-height:1}
.break-rule{position:absolute;left:180px;top:116px;width:162px;height:1px;background:rgba(255,255,255,.7)}
.break-quote{position:absolute;left:190px;top:120px;width:160px;font-family:"Shadows Into Light",cursive;font-size:11.5px;line-height:1.25;color:#f7dede}

/* slide 3 */
.pull-quote{border-top:1px solid #999;border-bottom:1px solid #999;padding:5px 0 9px;margin:7px 0;color:var(--red-bright);font-style:italic}

/* slide 4 */
.feature{position:absolute;top:80px;width:90px;text-align:center}
.feature-photo{width:68px;height:68px;margin:0 auto;border-radius:50%;border:4px solid var(--red);box-shadow:0 0 0 1px #ddd}
.feature h3{font-weight:400;font-size:9px;color:var(--orange);margin-top:9px}
.feature p{font-size:5.6px;line-height:1.35;text-align:left;margin:6px 0 0 8px}

/* slide 5 */
.chart{position:absolute;left:24px;top:60px}
.chart-caption{position:absolute;left:28px;top:176px;width:186px;font-size:5.5px;line-height:1.35}
.side-list{position:absolute;left:246px;top:36px;width:110px;list-style:none}
.side-list li{height:41px;font-size:4.3px;line-height:1.35;color:var(--ink)}
.side-list h4{font-weight:400;font-size:6.5px;color:var(--orange);margin-bottom:3px}

/* closing */
.social{position:absolute;top:137px;left:190px;display:flex;gap:6px}
.social span{width:17px;height:17px;border-radius:50%;background:#fff}
</style>
</head>
<body>

<!-- Cover -->
<section class="slide slide--red col-left row-1">
  <div class="ribbon"><div class="ribbon-base"></div></div>
  <h1 class="cover-title">Welcome</h1>
  <div class="cover-rule"></div>
  <p class="cover-name">Presentation name</p>
  <p class="cover-sub">Other text to be included here</p>
  <p class="cover-by">BY: DANA REYES</p>
  <span class="brand-mark" style="left:222px;top:179px">VentriLedger.Com</span>
</section>

<!-- Slide 1 -->
<section class="slide col-right row-1">
  <h2 class="slide-heading">Lorem ipsum.<small>Subtitle</small></h2>
  <div class="body-copy" style="left:27px;top:59px;width:162px">
    <p>Lorem ipsum dolor sit amet, consectetuer adipiscing elit, sed diam nonummy nibh euismod tincidunt ut laoreet dolore magna aliquam erat volutpat. Ut wisi enim ad minim veniam, quis nostrud exerci tation ullamcorper suscipit lobortis nisl ut aliquip ex ea commodo consequatdolore te feugait nulla facilisi.</p>
    <p>Expetenda tincidunt in sed, ex partem placerat sea, porro commodo ex eam. His putant aeterno interesset at. Usu ea mundi tincidunt, omnium virtute aliquando ius ex. Ea aperiri sententiae duo. Usu nullam dolorum quaestio ei, sit vidit facilisis ea. Per ne impedit iracundia neglegentur. Consetetur neglegentur eum ut, vis animal legimus inimicus id.</p>
  </div>
  <span class="dot" style="left:236px;top:27px"></span><span class="dot" style="left:243px;top:31px"></span><span class="dot" style="left:229px;top:31px"></span><span class="dot" style="left:236px;top:36px"></span><span class="dot" style="left:236px;top:44px"></span>
  <div class="avatar" role="img" aria-label="Portrait photo of a smiling woman" style="left:230px;top:50px;width:40px;height:40px"></div>
  <div class="callout" style="left:272px;top:70px;width:58px">Text here</div>
  <div class="avatar" role="img" aria-label="Portrait photo of a man" style="left:196px;top:92px;width:36px;height:36px"></div>
  <div class="callout" style="left:216px;top:114px;width:78px;padding-left:24px">Text here</div>
  <div class="body-copy" style="left:200px;top:157px;width:150px">
    <p>Lorem ipsum dolor sit amet, consectetuer adipiscing elit, sed diam nonummy nibh euismod tincidunt ut laoreet dolore magna aliquam erat volutpat. Ut wisi enim ad minim modo consequatdolore te feugait nulla facilisi.</p>
  </div>
  <footer class="slide-footer"><span class="footer-logo">VentriLedger.Com</span><div class="footer-title"><b>Presentation name</b><small>Other text to be included here</small></div><span class="footer-by">BY: DANA REYES</span><span class="page-num">1</span></footer>
</section>

<!-- Slide 2 -->
<section class="slide col-left row-2">
  <svg width="368" height="278" style="position:absolute;left:0;top:0"><path d="M0 0H212C206 120 190 200 142 247H0Z" fill="#c8192a"/></svg>
  <div class="bubble" style="left:80px;top:14px;width:98px;height:98px;padding:26px 14px 0 8px">Lorem ipsum dolor sit amet, con<b>nonummy nibh euismod</b> tac-cumsaugue duis dolore</div>
  <div class="avatar" role="img" aria-label="Portrait photo of a man" style="left:146px;top:70px;width:42px;height:42px"></div>
  <div class="bubble" style="left:40px;top:112px;width:102px;height:102px;padding:36px 20px 0 8px">Lorem ipsum dolor sit amet, con<b>nonummy nibh euismod</b> tac-cumsaugue duis dolore</div>
  <div class="avatar" role="img" aria-label="Portrait photo of a man" style="left:96px;top:182px;width:42px;height:42px"></div>
  <h2 class="slide-heading" style="left:225px;top:27px">Lorem ipsum.<small>Subtitle</small></h2>
  <div class="body-copy" style="left:225px;top:57px;width:130px">
    <p>Lorem ipsum dolor sit amet, consectetuer adipiscing elit, sed diam nonummy nibh euismod tincidunt ut laoreet dolore magna aliquam erat volutpat. Ut wisi enim ad minim veniam, quis nostrud exerci tation ullamcorper suscipit lobortis nisl ut aliquip ex ea commodo consequatdolore te feugait nulla facilisi.</p>
    <p>Expetenda tincidunt in sed, ex partem placerat sea, porro commodo ex eam. His putant aeterno interesset at. Usu ea mundi tincidunt, omnium virtute aliquando ius ex. Ea aperiri sententiae duo. Usu nullam dolorum quaestio ei, sit vidit facilisis ea. Per ne impedit iracundia neglegentur. Consetetur neglegentur eum ut, vis animal legimus inimicus id.</p>
  </div>
  <footer class="slide-footer"><span class="footer-logo">VentriLedger.Com</span><div class="footer-title"><b>Presentation name</b><small>Other text to be included here</small></div><span class="footer-by">BY: DANA REYES</span><span class="page-num">2</span></footer>
</section>

<!-- Break -->
<section class="slide slide--red col-right row-2">
  <div class="cup" role="img" aria-label="Line illustration of a steaming coffee cup"></div>
  <h2 class="break-title">Break time</h2>
  <div class="break-rule"></div>
  <p class="break-quote">“ It's a great way to re-fresh and re-energize your body and mind”</p>
  <footer class="slide-footer"><span class="footer-logo">VentriLedger.Com</span><div class="footer-title"><b>Presentation name</b><small>Other text to be included here</small></div><span class="footer-by">BY: DANA REYES</span></footer>
</section>

<!-- Slide 3 -->
<section class="slide col-left row-3">
  <h2 class="slide-heading">Lorem ipsum.<small>Subtitle</small></h2>
  <div class="body-copy" style="left:27px;top:61px;width:314px;font-size:5.8px">
    <p>Lorem ipsum dolor sit amet, consectetur adipiscing elit. Nullam a orci sit amet magna varius porttitor eu quis nisi. Ut viverra mi a leo lacinia molestie non sed quam. Pellentesque habitant morbi tristique senectus et netus et malesuada fames ac turpis egestas. Suspendisse tempor erat lorem, ac blandit libero porttitor vitae. Suspendisse faucibus nisl sed libero tristique, non luctus nulla viverra. Aenean porta quam sed accumsan imperdiet. Maecenas convallis auctor consectetur. Praesent posuere ullamcorper lectus sit amet viverra.</p>
    <p>Donec egestas nec leo in fringilla. Morbi sem metus, consequat non malesuada in, dictum nec elit. Phasellus quam eros, euismod ac enim vel, auctor dignissim ligula. Integer tempor tellus purus, ac cursus nisi sagittis pellentesque. Nullam luctus fermentum rhoncus.</p>
    <p class="pull-quote">Quisque commodo felis vitae aliquam bibendum. Curabitur sapien velit, egestas eget eros vitae, fermentum pellentesque sapien.</p>
    <p>Aliquam vitae turpis massa. Nulla pharetra massa lorem, eget egestas diam vehicula a. Mauris sed justo urna. Curabitur facilisis nibh eget sollicitudin varius. Pellentesque semper eros eu quam elementum egestas. Integer vitae elit tellus. Fusce vitae lacus porta, venenatis justo quis, auctor sapien. Morbi pretium sapien vel nibh bibendum cursus. Nullam ullamcorper urna vitae lacus posuere pretium. Fusce eget orci viverra, vehicula orci vel, vulputate lorem. Fusce sollicitudin accumsan tortor nec tincidunt.</p>
  </div>
  <footer class="slide-footer"><span class="footer-logo">VentriLedger.Com</span><div class="footer-title"><b>Presentation name</b><small>Other text to be included here</small></div><span class="footer-by">BY: DANA REYES</span><span class="page-num">3</span></footer>
</section>

<!-- Slide 4 -->
<section class="slide col-right row-3">
  <h2 class="slide-heading">Lorem ipsum.<small>Subtitle</small></h2>
  <div class="feature" style="left:17px">
    <div class="feature-photo" role="img" aria-label="Photo of a red apple with a stethoscope" style="background:radial-gradient(circle at 45% 45%,#e0303a,#7a1015 75%)"></div>
    <h3>Subtitle</h3><p>Lorem ipsum dolor sit amet, con<b>nonummy nibh euismod</b> taccum-saugue duis dolore</p>
  </div>
  <div class="feature" style="left:138px">
    <div class="feature-photo" role="img" aria-label="Photo of hands forming a heart shape" style="background:radial-gradient(circle at 50% 50%,#e2c4b4,#5e86b8 75%)"></div>
    <h3>Subtitle</h3><p>Lorem ipsum dolor sit amet, con<b>nonummy nibh euismod</b> taccum-saugue duis dolore</p>
  </div>
  <div class="feature" style="left:256px">
    <div class="feature-photo" role="img" aria-label="Photo of a stethoscope on a medical chart" style="background:radial-gradient(circle at 50% 50%,#f2f2f2,#8d8d8d 80%)"></div>
    <h3>Subtitle</h3><p>Lorem ipsum dolor sit amet, con<b>nonummy nibh euismod</b> taccum-saugue duis dolore</p>
  </div>
  <footer class="slide-footer"><span class="footer-logo">VentriLedger.Com</span><div class="footer-title"><b>Presentation name</b><small>Other text to be included here</small></div><span class="footer-by">BY: DANA REYES</span><span class="page-num">4</span></footer>
</section>

<!-- Slide 5 -->
<section class="slide col-left row-4">
  <h2 class="slide-heading">Lorem ipsum.<small>Subtitle</small></h2>
  <svg class="chart" width="195" height="112" viewBox="0 0 195 112" role="img" aria-label="Bar chart with six rising bars">
    <g fill="#c8192a">
      <rect x="2" y="85" width="28" height="16"/>
      <rect x="34" y="71" width="28" height="30"/>
      <rect x="66" y="61" width="28" height="40"/>
      <rect x="98" y="49" width="28" height="52"/>
      <rect x="130" y="35" width="28" height="66"/>
      <rect x="162" y="19" width="28" height="82"/>
    </g>
    <g font-family="Arimo, sans-serif" font-size="4.3" fill="#333" text-anchor="middle">
      <text x="16" y="109">OPCION 1</text><text x="48" y="109">OPCION 1</text><text x="80" y="109">OPCION 1</text><text x="112" y="109">OPCION 1</text><text x="144" y="109">OPCION 1</text><text x="176" y="109">OPCION 1</text>
    </g>
  </svg>
  <p class="chart-caption">Lorem ipsum dolor ipse salam in potim cepniae melion per dan ons quech canum vitus daiam in siesi on per manicoleis dalaq opcinz on dieu.</p>
  <ul class="side-list">
    <li><h4>Subtitle</h4>Lorem ipsum dolor sit amet, connonummy nibh euismodtaccumsaugue duis dolore.</li>
    <li><h4>Subtitle</h4>Lorem ipsum dolor sit amet, connonummy nibh euismodtaccumsaugue duis dolore.</li>
    <li><h4>Subtitle</h4>Lorem ipsum dolor sit amet, connonummy nibh euismodtaccumsaugue duis dolore.</li>
    <li><h4>Subtitle</h4>Lorem ipsum dolor sit amet, connonummy nibh euismodtaccumsaugue duis dolore.</li>
  </ul>
  <footer class="slide-footer"><span class="footer-logo">VentriLedger.Com</span><div class="footer-title"><b>Presentation name</b><small>Other text to be included here</small></div><span class="footer-by">BY: DANA REYES</span><span class="page-num">5</span></footer>
</section>

<!-- Closing -->
<section class="slide slide--red col-right row-4">
  <div class="ribbon"><div class="ribbon-base"></div></div>
  <h2 class="cover-title" style="left:130px;top:86px;font-size:32px">Thank you</h2>
  <div class="cover-rule" style="left:130px;top:119px;width:176px"></div>
  <div class="social" aria-label="Social media links"><span></span><span></span><span></span><span></span><span></span></div>
  <span class="brand-mark" style="left:222px;top:179px">VentriLedger.Com</span>
</section>

</body>
</html>
```